PLMT stationery 2023

Our stationery dates back to 2007 when we changed practice rooms.
We would like to have kept the logo and spiced up the design, especially since we have one more colleague (Dr. Liselotte Brunnhuber)
Our practice colors are a slightly more muted pink and sand-colored.
Follow-up orders for flyers, notices, etc. are still waiting for this design.

```html
<!DOCTYPE html>
<html lang="de">
<head>
<meta charset="utf-8">
<title>PLMT Briefpapier</title>
<link rel="stylesheet" href="https://fonts.googleapis.com/css2?family=Arimo:wght@400;700&family=Source+Sans+3:wght@400&family=Josefin+Sans:wght@400&display=swap">
<style>
  :root {
    --backdrop: #dedede;
    --paper: #ffffff;
    --ink-dark: #1c1a1c;
    --ink-grey: #666666;
    --ink-soft: #8a8a8a;
    --accent: #e2c800;
    --accent-faint: #fff8c4;
    --rule: #9a9a9a;
  }
  html, body {
    margin: 0;
    width: 1200px;
    height: 1200px;
    overflow: hidden;
    background: var(--backdrop);
  }
  .letterhead {
    position: absolute;
    left: 235px;
    top: 84px;
    width: 912px;
    height: 1290px;
    background: var(--paper);
    transform: scale(0.8);
    transform-origin: 0 0;
    font-family: "Arimo", Arial, sans-serif;
    overflow: hidden;
  }
  .abs { position: absolute; }
  .bar-dark { left: 0; top: 150px; width: 912px; height: 7px; background: var(--ink-dark); }
  .bar-accent { left: 0; top: 163px; width: 912px; height: 3px; background: var(--accent); }
  .brand {
    left: 40px; top: 96px; width: 315px; height: 64px;
    background: var(--paper);
    font-family: "Josefin Sans", sans-serif;
    font-size: 70px; line-height: 70px;
    color: var(--ink-dark);
    padding-left: 10px;
    letter-spacing: 2px;
  }
  .brand-dot { display: inline-block; width: 14px; height: 14px; border-radius: 50%; background: var(--accent); margin-left: 10px; vertical-align: 10px; }
  .physicians {
    right: 295px; top: 45px; text-align: right;
    font-weight: 700; font-size: 14.5px; line-height: 18.5px; color: var(--ink-grey);
  }
  .divider { left: 630px; top: 50px; width: 1px; height: 86px; background: var(--rule); }
  .contacts {
    left: 641px; top: 45px; margin: 0; padding: 0; list-style: none;
    font-family: "Source Sans 3", sans-serif; font-size: 14.5px; line-height: 18.5px; color: var(--ink-grey);
  }
  .contacts li { display: flex; align-items: center; gap: 6px; }
  .contacts svg { width: 12px; height: 12px; }
  .contacts .address { margin-left: 0; padding-top: 1px; }
  .salutation { left: 84px; top: 396px; font-size: 20px; font-weight: 700; color: var(--ink-soft); }
  .body-copy { left: 81px; top: 457px; width: 750px; font-size: 15px; line-height: 18.8px; color: var(--ink-soft); }
  .body-copy p { margin: 0 0 16px; }
  .closing { left: 83px; top: 844px; font-size: 11px; font-weight: 700; color: var(--ink-grey); }
  .signature { left: 85px; top: 900px; width: 115px; height: 36px; background: #ececec; border-radius: 4px; }
  .illustration {
    left: 170px; top: 855px; width: 742px; height: 330px;
    background: radial-gradient(ellipse at 45% 50%, var(--accent-faint) 0%, rgba(255,248,196,0.5) 55%, rgba(255,255,255,0) 80%);
  }
  .hours { left: 0; width: 912px; top: 1193px; text-align: center; font-size: 18px; font-weight: 700; color: var(--ink-grey); }
  .hours-rule { left: 72px; top: 1220px; width: 768px; height: 1px; background: var(--rule); }
  .services { left: 0; width: 912px; top: 1227px; text-align: center; font-size: 15px; line-height: 18.5px; color: var(--ink-grey); }
  .services span::before { content: "•"; color: var(--accent); margin: 0 4px 0 6px; }
</style>
</head>
<body>
<main class="letterhead">
  <div class="abs bar-dark"></div>
  <div class="abs bar-accent"></div>
  <div class="abs brand">PLMT<span class="brand-dot"></span></div>

  <div class="abs physicians">
    Dr. Helga Marwitz<br>
    Dr. Petra Lindauer<br>
    Dr. Stefan Marwitz<br>
    Dr. Ildikó Varga<br>
    Dr. Liselotte Brunnhuber
  </div>
  <div class="abs divider"></div>
  <ul class="abs contacts">
    <li><svg viewBox="0 0 12 12"><path d="M2 1l2 0 1 3-1.5 1a6 6 0 0 0 3.5 3.5l1-1.5 3 1 0 2c0 .6-.4 1-1 1A10 10 0 0 1 1 2c0-.6.4-1 1-1z" fill="var(--accent)"/></svg>044/318 52 40</li>
    <li><svg viewBox="0 0 12 12"><rect x="3" y="1" width="6" height="3" fill="var(--accent)"/><rect x="1" y="5" width="10" height="5" rx="1" fill="var(--accent)"/><rect x="3" y="8" width="6" height="3" fill="#fff" stroke="var(--accent)"/></svg>044/318 52 41</li>
    <li><svg viewBox="0 0 12 12"><rect x="1" y="3" width="10" height="7" fill="var(--accent)"/><path d="M1 3l5 4 5-4" stroke="#fff" fill="none"/></svg>praxis.plmt@hin.ch</li>
    <li><svg viewBox="0 0 12 12"><circle cx="6" cy="6" r="5" fill="var(--accent)"/><path d="M1 6h10M6 1c2 2 2 8 0 10M6 1c-2 2-2 8 0 10" stroke="#fff" fill="none" stroke-width="0.8"/></svg>www.praxis-plmt.ch</li>
    <li class="address">Ahornweg 14, 8400 Winterthur</li>
  </ul>

  <div class="abs salutation">Dear Mr. Keller,</div>
  <div class="abs body-copy">
    <p>Lorem ipsum dolor sit amet, consectetuer adipiscing elit, sed diam nonmmy nibh euismod tincidunt ut laor eet dolore magna aliquam erat volutpat. Ut wisi enim ad minim veniam, quis nostrud exerci tationmcorper suscipit lobortis nisl ut aliquip ex ea commodo consequat. Duis autem vel eum iriure dolor in hendrerit in vulputate velit esse molestie consequat, vel illum dolore eu feugiat</p>
    <p>Rorem ipsum dolor sit amet, consectetuer adipiscing elit, sed diam nonmmy nibh euismod tincidunt ut laor eet dolore magna aliquam erat volutpat. Ut wisi enim ad minim veniam, quis nostrud exerci tationmcorper suscipit lobortis nisl ut aliquip ex ea commodo consequat. Duis autem vel eum iriure dolor in hendrerit in vulputate velit esse molest</p>
    <p>Dorem ipsum dolor sit amet, consectetuer adipiscing elit, sed diam nonmmy nibh euismod tincidunt ut laor eet dolore magna aliquam erat volutpat. Ut wisi enim ad minim veniam, quis nostrud exerci tationmcorper suscipit lobortis nisl ut aliquip ex ea commodo consequat. Duis autem vel eum iriure dolor in hendrerit in suscipit lobortis nisl ut aliquip ex ea commodo consequat. Duis autem vel eum iriure dolor in hendrerit in vulputate velit esse molestie consequat, vel illum</p>
    <p>Sorem ipsum dolor sit amet, consectetuer adipiscing elit, sed diam nonmmy nibh euismod tincidunt ut laor eet dolore magna aliquam erat volutpat. Ut wisi enim ad minim veniam, quis nostrud exerci tationmcorper suscipit lobortis nisl ut aliquip ex ea commodo consequat. Duis autem vel eum iriure dolor in</p>
  </div>

  <div class="abs illustration" role="img" aria-label="Faint yellow sketch of three women walking in front of the practice building"></div>
  <div class="abs closing">Sincerely,</div>
  <div class="abs signature" role="img" aria-label="Handwritten signature"></div>

  <div class="abs hours">Öffnungszeiten NEU: Montag - Freitag 08.00 - 12.00 Uhr und 13.00 - 17.00 Uhr</div>
  <div class="abs hours-rule"></div>
  <div class="abs services">
    <span>Fachärzte für Gynäkologie und Geburtshilfe</span> <span>Pränataldiagnostik</span><br>
    <span>Schwangerschaftsbetreuung</span> <span>Kinderwunschbehandlung</span> <span>Ambulante Operationen</span> <span>Onkologische Betreuung</span>
  </div>
</main>
</body>
</html>
```